Flyer-Design für den Vertrieb von Sitzbänken
Zielgruppe
Vertrieb von Valmix Sitzbänken , sich auf unsere Webseite stützen www.kerlotechnik.ch,für Grundinfos.
Aufgabenstellung
Wir wollen einen Flyer haben welcher die Verschmelzung von ländlichen Umgebung und einer moderner Stadt (Smart City) darstellt. Die Sitzbank mit dem Monitor soll integriert werden und die Benefits wie :
Solarenergie,USB- und induktive Ladestation, W-Lan Internet, Nachtbeleuchtung, Monitor als Werbungsfläche müssen mit (Symbolen) aufgeführt und abgebildet. Weitere infos können auch bei www.pramvo.eu abgeholt werden.

```html
<!DOCTYPE html>
<html lang="de">
<head>
<meta charset="utf-8">
<title>KERLO Solutions – Valmix Sitzbank</title>
<link href="https://fonts.googleapis.com/css2?family=EB+Garamond:wght@400&display=swap" rel="stylesheet">
<style>
  :root {
    --bg: #000000;
    --text: #ffffff;
    --accent: #1fc63a;
    --brand: #3aa845;
    --footer-text: #141414;
    --photo-dark: #050508;
    --photo-glow: #2c2366;
    --photo-light: #a9b2b6;
  }
  * { margin: 0; padding: 0; box-sizing: border-box; }
  html, body { width: 848px; height: 1200px; overflow: hidden; background: var(--bg); }
  .flyer {
    position: relative; width: 848px; height: 1200px; overflow: hidden;
    background: var(--bg); color: var(--text);
    font-family: "EB Garamond", Georgia, serif;
  }
  .brand {
    position: absolute; left: 30px; top: 40px;
    display: flex; align-items: center; gap: 16px;
  }
  .brand-dot { width: 94px; height: 94px; border-radius: 50%; background: var(--brand); }
  .brand-name { font-size: 44px; line-height: 1; color: var(--text); letter-spacing: 1px; }

  .feature-icon { position: absolute; fill: none; stroke: var(--text); }
  .feature { position: absolute; left: 152px; width: 584px; }
  .feature-title {
    font-weight: 400; font-size: 29px; line-height: 36px;
    padding-bottom: 6px; border-bottom: 2px solid var(--accent);
  }
  .feature-text { font-size: 17.5px; line-height: 20.6px; margin-top: 18px; }
  .feature-text span { display: block; white-space: nowrap; }
  .feature-text.justified span { text-align: justify; text-align-last: justify; white-space: normal; }
  .feature-text.justified span:last-child { text-align-last: left; }

  .feature-wifi { top: 206px; }
  .feature-solar { top: 414px; }
  .feature-monitor { top: 607px; left: 150px; }

  .bench-photo {
    position: absolute; left: 0; top: 790px; width: 848px; height: 410px;
    background: linear-gradient(165deg, var(--photo-dark) 28%, var(--photo-glow) 52%, var(--photo-light) 100%);
  }

  .footer {
    position: absolute; right: 21px; bottom: 3px;
    font-size: 16px; color: var(--footer-text); white-space: nowrap;
  }
</style>
</head>
<body>
<div class="flyer">
  <div class="brand">
    <div class="brand-dot"></div>
    <div class="brand-name">KERLO Solutions</div>
  </div>

  <svg class="feature-icon" style="left:56px;top:212px" width="46" height="34" viewBox="0 0 46 34" aria-hidden="true">
    <path d="M3 12 A28 28 0 0 1 43 12" stroke-width="4" stroke-linecap="round"/>
    <path d="M9 19 A19 19 0 0 1 37 19" stroke-width="4" stroke-linecap="round"/>
    <path d="M15 25 A11 11 0 0 1 31 25" stroke-width="4" stroke-linecap="round"/>
    <circle cx="23" cy="30" r="3.5" fill="#fff" stroke="none"/>
  </svg>
  <svg class="feature-icon" style="left:57px;top:270px" width="44" height="24" viewBox="0 0 44 24" aria-hidden="true">
    <path d="M2 12 H36" stroke-width="3"/>
    <path d="M2 12 L8 7 V17 Z" fill="#fff"/>
    <circle cx="38" cy="12" r="5" fill="#fff" stroke="none"/>
    <path d="M12 12 L18 4 H26" stroke-width="3"/>
    <circle cx="28" cy="4" r="3" fill="#fff" stroke="none"/>
    <path d="M17 12 L22 20 H27" stroke-width="3"/>
    <rect x="26" y="17" width="6" height="6" fill="#fff" stroke="none"/>
  </svg>
  <section class="feature feature-wifi">
    <h2 class="feature-title">W-LAN &amp; USB</h2>
    <p class="feature-text">
      <span>Valmix Standard ist zu 100% solarbetrieben und benötigt keine zusätzliche Strom-</span>
      <span>versorgung oder Infrastrukturellen Arbeitsaufwand. Ein speziell entwickelter Regler</span>
      <span>erzeugt 30% mehr Ausgangsleistung. An Wintertagen überwacht er die Wetterbe-</span>
      <span>dingungen und schaltet die Bank bei schlechtem Wetter ab. Der öffentliche Raum</span>
      <span>bekommt durch das Design eine persönliche und attraktive Note.</span>
    </p>
  </section>

  <svg class="feature-icon" style="left:52px;top:414px" width="56" height="48" viewBox="0 0 56 48" aria-hidden="true">
    <circle cx="18" cy="18" r="9" fill="#fff" stroke="none"/>
    <g stroke-width="3" stroke-linecap="round">
      <path d="M18 2 V5"/><path d="M18 31 V34"/><path d="M2 18 H5"/><path d="M31 18 H34"/>
      <path d="M7 7 L9 9"/><path d="M27 27 L29 29"/><path d="M7 29 L9 27"/><path d="M27 9 L29 7"/>
    </g>
    <path d="M38 12 H52 V20 A7 7 0 0 1 38 20 Z" fill="#fff" stroke="none"/>
    <path d="M41 6 V12 M49 6 V12" stroke-width="3"/>
    <path d="M45 27 V38 A5 5 0 0 1 40 43 H30 L27 40 L24 43 H20 A4 4 0 0 1 16 39 V30" stroke-width="3"/>
  </svg>
  <section class="feature feature-solar">
    <h2 class="feature-title">Solarenergie</h2>
    <p class="feature-text">
      <span>Valmix Standard ist zu 100% solarbetrieben und benötigt keine zusätzliche Strom-</span>
      <span>versorgung oder Infrastrukturellen Arbeitsaufwand. Ein speziell entwickelter Regler</span>
      <span>erzeugt 30% mehr Ausgangsleistung und überwacht an Wintertagen das Wetter.</span>
    </p>
  </section>

  <svg class="feature-icon" style="left:54px;top:615px" width="46" height="36" viewBox="0 0 46 36" aria-hidden="true">
    <rect x="2" y="2" width="42" height="27" rx="2" stroke-width="3"/>
    <path d="M17 33 H29" stroke-width="3"/>
    <path d="M23 29 V33" stroke-width="3"/>
  </svg>
  <section class="feature feature-monitor">
    <h2 class="feature-title">Monitor als Werbungsfläche</h2>
    <p class="feature-text justified">
      <span>Das besondere Merkmal von Valmix Urban ist ein superheller 19 Zoll Bildschirm der</span>
      <span>für das Anzeigen von Videos, Bildern oder unterschiedlicher Informationen in der</span>
      <span>Öffentlichkeit dienen kann (z. B. Wetterdaten).</span>
    </p>
  </section>

  <div class="bench-photo" role="img" aria-label="Foto: beleuchtete Valmix Solar-Sitzbank mit Smartphone auf der Ladefläche"></div>

  <div class="footer">KERLO Solutions , CH-4812 Talmatt,info@kerlotechnik.ch, www.kerlotechnik.ch</div>
</div>
</body>
</html>
```